Quorlan Visit cards serious but not sad

Hello, I'd like to design my visit cards with the logo Quorlan (attached) the following information: Name: Mathis Deloraux Title: Mobile Director: 33 (0) 6 28 40 13 85 Phone: 33 (0) 4 71 86 52 09 e-mail: mathis.deloraux@quorlan-advisory.example address: 17 Rue Anatole Berrin 92400 Courbevoie This visit will be used on the banking institutions and Quorlan is a consulting firm. I do not want to have dark background.

Target Market(s)

banks

Contact Information for Business Card

Name : Mathis Deloraux
Title : Director
mobile : +33(0)6 28 40 13 85
Phone : +33(0)4 71 86 52 09
e-mail: mathis.deloraux@quorlan-advisory.example
adresse : 17 Rue anatole Berrin 92870 Valmoreuil

Requirements
Nice to have
• serious but not sad

```html
<!DOCTYPE html>
<html lang="en">
<head>
<meta charset="utf-8">
<title>Quorlan – Business Card</title>
<link rel="stylesheet" href="https://fonts.googleapis.com/css2?family=Roboto:wght@300;400;700&family=Roboto+Condensed:wght@400;700&display=swap">
<style>
  :root {
    --brand-blue: #0b74c4;
    --ink: #3c3c3c;
    --muted: #9a9a9a;
    --card-white: #ffffff;
    --pattern-tint: rgba(214, 230, 245, 0.75);
    --backdrop: #eceae6;
  }
  * { box-sizing: border-box; margin: 0; padding: 0; }
  html, body {
    width: 1200px; height: 950px; overflow: hidden;
    background: var(--backdrop);
    font-family: "Roboto", Arial, sans-serif;
  }
  .stage { position: relative; width: 1200px; height: 950px; }
  .card {
    position: absolute; top: 307px;
    width: 520px; height: 336px;
    border-radius: 14px;
    box-shadow: 0 6px 18px rgba(0,0,0,0.15);
    overflow: hidden;
  }
  .card--front { left: 70px; background: var(--card-white); }
  .card--back  { left: 610px; background: var(--brand-blue); }

  .circuit-pattern {
    position: absolute; inset: 0;
    background: radial-gradient(ellipse 70% 75% at 78% 72%, var(--pattern-tint) 0%, rgba(214,230,245,0.3) 55%, rgba(255,255,255,0) 100%);
  }

  .brand {
    position: absolute; right: 36px; top: 36px;
    display: flex; align-items: center; gap: 12px;
  }
  .brand__dot {
    width: 50px; height: 50px; border-radius: 50%;
    background: var(--brand-blue);
  }
  .brand__name {
    font-weight: 400; font-size: 46px; letter-spacing: 0.5px;
    color: var(--brand-blue); line-height: 1;
  }

  .contact {
    position: absolute; left: 30px; bottom: 26px;
    font-family: "Roboto Condensed", "Arial Narrow", sans-serif;
  }
  .contact__name {
    font-weight: 700; font-size: 23px; color: var(--brand-blue);
    text-transform: uppercase; letter-spacing: 0.3px; line-height: 1.1;
  }
  .contact__title {
    font-size: 14px; color: var(--muted); text-transform: uppercase;
    letter-spacing: 1px; margin: 2px 0 8px;
  }
  .contact__list { list-style: none; }
  .contact__item {
    display: flex; align-items: center; gap: 9px;
    font-size: 13px; color: var(--ink); line-height: 19px;
  }
  .contact__icon { width: 13px; height: 13px; fill: var(--brand-blue); flex: none; }
  .contact__address { font-size: 15px; color: var(--ink); margin-top: 6px; }
</style>
</head>
<body>
<main class="stage">
  <section class="card card--front" aria-label="Business card front">
    <div class="circuit-pattern" role="img" aria-label="Faint pale blue circuit-line pattern"></div>

    <div class="brand">
      <span class="brand__dot"></span>
      <span class="brand__name">quorlan</span>
    </div>

    <div class="contact">
      <h1 class="contact__name">Mathis Deloraux</h1>
      <p class="contact__title">Director</p>
      <ul class="contact__list">
        <li class="contact__item">
          <svg class="contact__icon" viewBox="0 0 16 16" aria-hidden="true"><path d="M3.5 1l2.5 3-1.5 2c1 2 3 4 5 5l2-1.5 3 2.5-1.5 2.5C8 14.5 1.5 8 1 2.5z"/></svg>
          +33(0)4 71 86 52 09
        </li>
        <li class="contact__item">
          <svg class="contact__icon" viewBox="0 0 16 16" aria-hidden="true"><path d="M4 1h8v14H4zM5.5 2.5v9h5v-9z"/></svg>
          +33(0)6 28 40 13 85
        </li>
        <li class="contact__item">
          <svg class="contact__icon" viewBox="0 0 16 16" aria-hidden="true"><path d="M1 3h14v10H1zM2.5 4.5L8 9l5.5-4.5z"/></svg>
          mathis.deloraux@quorlan-advisory.example
        </li>
        <li class="contact__item">
          <svg class="contact__icon" viewBox="0 0 16 16" aria-hidden="true"><circle cx="8" cy="8" r="7"/><path d="M1 8h14M8 1c-3 3.5-3 10.5 0 14M8 1c3 3.5 3 10.5 0 14" stroke="#fff" stroke-width="1" fill="none"/></svg>
          www.quorlan-advisory.example
        </li>
      </ul>
      <p class="contact__address">17 Rue anatole Berrin, 92870 Valmoreuil</p>
    </div>
  </section>

  <section class="card card--back" aria-label="Business card back"></section>
</main>
</body>
</html>
```